Pixel Harbor Business Card

I have attached several examples of business cards that I have seen online that I liked. We will be incorporating Spot UV coating and raised ink on the cards. Optionally we may use embossing with color. The business card will be used for 3d printing services. We are hoping to see some different color options of cards (i.e. black card, white card, etc.). We look forward to your ideas.

• Dorian Kest
Founder and CEO
+1.555.000.0000 cell
+1.000.000.0001 office
+1.000.000.0001 fax
Dorian.Kest@3dVorlanix.example
www.3dVorlanix.example
• I would be nice to see some 3d background designs to add some depth to the designs of the cards since it is a 3d design company. There are examples of this in the files I have attached.

```html
<!DOCTYPE html>
<html lang="en">
<head>
<meta charset="utf-8">
<title>Vorlanix Business Card</title>
<link rel="stylesheet" href="https://fonts.googleapis.com/css2?family=Exo+2:wght@300;400;700;800&display=swap">
<style>
  :root {
    --paper: #ece8e7;
    --ink-dark: #2b2b2b;
    --mark: #3a3a3a;
    --card-dark: #2c2c2c;
    --card-dark-edge: #1c1c1c;
    --accent-blue: #1f9ddb;
    --text-light: #ffffff;
  }
  * { margin: 0; padding: 0; box-sizing: border-box; }
  html, body {
    width: 720px;
    height: 1200px;
    overflow: hidden;
    background: var(--paper);
  }
  .card {
    position: relative;
    width: 720px;
    height: 1200px;
    font-family: "Exo 2", sans-serif;
  }
  .brand-panel {
    position: absolute;
    left: 0; top: 0;
    width: 720px; height: 640px;
    background: var(--paper);
  }
  .brand-dot {
    position: absolute;
    left: 284px; top: 140px;
    width: 152px; height: 152px;
    border-radius: 50%;
    background: var(--mark);
  }
  .brand-name {
    position: absolute;
    left: 0; top: 380px;
    width: 720px;
    text-align: center;
    font-weight: 300;
    font-size: 54px;
    letter-spacing: 14px;
    color: var(--ink-dark);
  }
  .contact-panel {
    position: absolute;
    left: 0; top: 640px;
    width: 720px; height: 560px;
    background: radial-gradient(ellipse at 40% 40%, var(--card-dark) 0%, var(--card-dark-edge) 100%);
  }
  .person-name {
    position: absolute;
    left: 78px; top: 640px;
    font-weight: 800;
    font-size: 82px;
    line-height: 80px;
    color: var(--accent-blue);
    letter-spacing: 1px;
  }
  .person-title {
    position: absolute;
    left: 84px; top: 805px;
    font-weight: 400;
    font-size: 26px;
    color: var(--text-light);
    letter-spacing: 1px;
  }
  .contact-list {
    position: absolute;
    left: 80px; top: 888px;
    width: 392px;
    list-style: none;
    color: var(--text-light);
    font-weight: 400;
    font-size: 28px;
  }
  .contact-list li {
    display: flex;
    justify-content: space-between;
    height: 44px;
    line-height: 44px;
    white-space: nowrap;
  }
  .contact-at { color: var(--accent-blue); }
  .contact-web { letter-spacing: 5px; }
</style>
</head>
<body>
  <main class="card">
    <section class="brand-panel">
      <div class="brand-dot"></div>
      <div class="brand-name">VORLANIX</div>
    </section>

    <section class="contact-panel" role="img" aria-label="Dark perforated metal texture background"></section>

    <h1 class="person-name">DORIAN<br>KEST</h1>
    <p class="person-title">FOUNDER AND CEO</p>

    <ul class="contact-list">
      <li><span>+1.555-000-0000</span><span>Cell</span></li>
      <li><span>+1.000-000-0001</span><span>Office</span></li>
      <li><span>+1.000-000-0002</span><span>Fax</span></li>
      <li><span>Dorian.Kest<span class="contact-at">@</span>3dVorlanix.example</span></li>
      <li class="contact-web"><span>WWW.3dVorlanix.example</span></li>
    </ul>
  </main>
</body>
</html>
```